KTR Engineering Business Card Design

We’re looking for an elegant, clean, and timeless business card design that communicates experience, capability, and reliability.

KTR Engineering was established in 1995 , we are a Government Contracting company providing Professional Services to the Ministry of Harbor Works, Frontier Stewardship and the Waypoint Consortium. Our capabilities include: Acquisition & Program Management; Intelligence & Security Operations; Cyber, IT & Network Operations; Lifecycle Logistics & Asset Readiness; C5ISR Systems Engineering & Sustainment.

We want the card to reflect a straightforward, confident approach to business. The design should feel polished and professional without being flashy or overly corporate.

Design Direction
Clean, sophisticated, and uncluttered
Elegant but understated
Strong typography and thoughtful spacing
A timeless aesthetic rather than something overly trendy
Confident and established, with a sense of substance
Easy to read and practical in a real-world business setting

The overall impression should be: “These are experienced professionals who know what they’re doing, do what they say, and can be relied upon.”

We’re open to creative interpretations. The finished card should feel distinctive through its typography, proportions, layout, and attention to detail rather than through excessive graphics or visual effects.

We’re looking for a design that would make a potential client immediately feel that they’re dealing with a capable, trustworthy, and established company.

Company Colors: Navy and Gold/Yellow (but you do not need to use these colors on the card)
Company Name: KTR Engineering Associates, Inc. (known as KTR Engineering)
Website: ktrengineering.example
Company Logo: Navy & Gold (other variations attached)

```html
<!DOCTYPE html>
<html lang="en">
<head>
<meta charset="utf-8">
<title>KTR Engineering – Business Card</title>
<link rel="stylesheet" href="https://fonts.googleapis.com/css2?family=Poppins:wght@400;500;800&family=Great+Vibes&display=swap">
<style>
  :root {
    --navy: #1c2557;
    --navy-logo: #212f63;
    --gold: #f5e34b;
    --paper: #ffffff;
    --mist: #e6e7e8;
    --backdrop: #d6d6d6;
    --ink-light: #ffffff;
  }
  html, body {
    margin: 0;
    padding: 0;
    width: 1200px;
    height: 2185px;
    overflow: hidden;
    background: var(--backdrop);
  }
  .canvas {
    position: relative;
    width: 1200px;
    height: 2185px;
  }
  .card {
    position: absolute;
    left: 97.5px;
    width: 1005px;
    height: 572.4px;
    display: block;
  }
  .card--front { top: 886px; }
  .card--back { top: 1507px; }
  .fill-navy { fill: var(--navy); }
  .fill-gold { fill: var(--gold); }
  .fill-paper { fill: var(--paper); }
  .fill-mist { fill: var(--mist); }
  .wordmark {
    font-family: 'Poppins', sans-serif;
    font-weight: 800;
    fill: var(--navy-logo);
    letter-spacing: -2px;
  }
  .established {
    font-family: 'Poppins', sans-serif;
    font-weight: 500;
    font-size: 25px;
    letter-spacing: 6px;
    fill: var(--gold);
  }
  .contact-text {
    font-family: 'Poppins', sans-serif;
    font-weight: 500;
    font-size: 26px;
    fill: var(--navy);
  }
  .years {
    font-family: 'Great Vibes', cursive;
    font-size: 76px;
    fill: var(--gold);
  }
  .tagline, .service-text {
    font-family: 'Poppins', sans-serif;
    font-weight: 400;
    fill: var(--ink-light);
  }
  .tagline { font-size: 20.5px; }
  .service-text { font-size: 21.5px; }
  .rule-gold { stroke: var(--gold); stroke-width: 1.5; }
  .rule-dotted { stroke: var(--gold); stroke-width: 1.5; stroke-dasharray: 3 4; }
  .icon-line { fill: none; stroke: var(--navy); stroke-width: 2.5; stroke-linecap: round; }
</style>
</head>
<body>
<main class="canvas">

  <!-- Front of card -->
  <svg class="card card--front" viewBox="0 0 1185 675" role="group" aria-label="Card front: KTR Engineering, established 1995">
    <rect class="fill-paper" width="1185" height="675"/>
    <path class="fill-mist" d="M715,0 L825,0 C720,40 630,110 585,175 C615,105 665,45 715,0 Z"/>
    <path class="fill-mist" d="M0,580 C300,640 550,620 740,580 C640,630 590,650 535,675 L0,675 Z"/>
    <path class="fill-navy" d="M825,0 L1185,0 L1185,445 C1120,560 1040,630 960,675 L535,675 C760,620 960,500 1015,330 C1050,200 950,120 820,125 C700,128 600,170 520,220 C580,130 690,50 825,0 Z"/>
    <path class="fill-mist" d="M1185,565 L1185,675 L1040,675 C1100,640 1150,605 1185,565 Z"/>
    <path class="fill-gold" d="M0,460 C80,520 180,570 295,590 C180,588 80,565 0,522 Z"/>
    <text class="established" x="930" y="45">ESTABLISHED</text>
    <text class="established" x="930" y="72">1995</text>
    <text class="wordmark" x="392" y="475" font-size="172">KTR</text>
  </svg>

  <!-- Back of card -->
  <svg class="card card--back" viewBox="0 0 1185 675" role="group" aria-label="Card back: contact details and capabilities">
    <rect class="fill-paper" width="1185" height="675"/>
    <path class="fill-navy" d="M495,0 L1185,0 L1185,675 L430,675 C560,600 660,480 680,340 C690,220 650,120 495,0 Z"/>
    <path class="fill-gold" d="M325,0 L495,0 C575,45 620,90 640,142 C580,80 470,30 325,0 Z"/>
    <path class="fill-mist" d="M705,320 C700,480 650,600 590,675 L690,675 C720,560 720,440 705,320 Z"/>

    <text class="wordmark" x="120" y="228" font-size="116">KTR</text>

    <!-- contact rows -->
    <g class="contact">
      <path class="fill-gold" d="M65,348 A30,30 0 0 1 125,348 L125,380 L65,380 Z"/>
      <path class="icon-line" d="M87,340 C86,356 96,366 110,366 L110,360 L103,356 L99,359 C95,357 92,354 91,350 L94,346 L90,339 Z"/>
      <text class="contact-text" x="142" y="360">555 014 2290</text>
      <line class="rule-dotted" x1="142" y1="388" x2="470" y2="388"/>

      <rect class="fill-gold" x="65" y="398" width="60" height="62"/>
      <circle class="icon-line" cx="95" cy="429" r="11"/>
      <ellipse class="icon-line" cx="95" cy="429" rx="5" ry="11"/>
      <line class="icon-line" x1="84" y1="429" x2="106" y2="429"/>
      <text class="contact-text" x="142" y="433">ktrengineering.example</text>
      <line class="rule-dotted" x1="142" y1="465" x2="470" y2="465"/>

      <path class="fill-gold" d="M65,475 L125,475 L125,505 A30,30 0 0 1 65,505 Z"/>
      <path class="fill-navy" d="M95,522 C88,512 84,506 84,499 A11,11 0 0 1 106,499 C106,506 102,512 95,522 Z"/>
      <circle class="fill-gold" cx="95" cy="499" r="4"/>
      <text class="contact-text" x="142" y="495">1480 Harbor Crest Avenue, Suite</text>
      <text class="contact-text" x="142" y="528">310 Bayview, VA 20000</text>
    </g>

    <!-- headline -->
    <text class="years" x="750" y="105">30 Years</text>
    <text class="tagline" x="740" y="148">CLEARED EXPERTISE WITH</text>
    <text class="tagline" x="740" y="170">MEASURABLE IMPACT</text>
    <line class="rule-gold" x1="742" y1="185" x2="1020" y2="185"/>

    <!-- capabilities -->
    <g class="services">
      <circle class="fill-gold" cx="768" cy="276" r="27"/>
      <circle class="icon-line" cx="768" cy="276" r="10"/>
      <text class="service-text" x="813" y="271">ACQUISITION &amp; PROGRAM</text>
      <text class="service-text" x="813" y="297">MANAGEMENT</text>
      <line class="rule-gold" x1="813" y1="316" x2="1115" y2="316"/>

      <circle class="fill-gold" cx="768" cy="356" r="27"/>
      <circle class="icon-line" cx="768" cy="356" r="10"/>
      <text class="service-text" x="813" y="351">INTELLIGENCE &amp; SECURITY</text>
      <text class="service-text" x="813" y="377">OPERATIONS</text>
      <line class="rule-gold" x1="813" y1="396" x2="1115" y2="396"/>

      <circle class="fill-gold" cx="768" cy="436" r="27"/>
      <circle class="icon-line" cx="768" cy="436" r="10"/>
      <text class="service-text" x="813" y="431">CYBER, IT &amp; NETWORK</text>
      <text class="service-text" x="813" y="457">OPERATIONS</text>
      <line class="rule-gold" x1="813" y1="480" x2="1115" y2="480"/>

      <circle class="fill-gold" cx="768" cy="518" r="27"/>
      <circle class="icon-line" cx="768" cy="518" r="10"/>
      <text class="service-text" x="813" y="513">LIFECYCLE LOGISTICS &amp;</text>
      <text class="service-text" x="813" y="539">ASSET READINESS</text>
      <line class="rule-gold" x1="813" y1="558" x2="1115" y2="558"/>

      <circle class="fill-gold" cx="768" cy="596" r="27"/>
      <circle class="icon-line" cx="768" cy="596" r="10"/>
      <text class="service-text" x="813" y="591">C5ISR SYSTEMS ENGINEERING</text>
      <text class="service-text" x="813" y="617">&amp; SUSTAINMENT</text>
    </g>
  </svg>

</main>
</body>
</html>
```